Business Card Design Project

Colette Marvaux logo on front of card with 'of Sydney' added in small font.
Back of card needs to include the following information :

"Pure pleasure for the discerning gentleman" (I may omit once I've seen the design)

colettemarvaux.com.au

Contact by SMS or email only :

colette@colettemarvaux.com.au
Mobile : 0483 615 204 or + 61 483 615 204

Target Market(s)

Male professionals aged 20-60.

Industry/Entity Type

Business

Requirements
Must have
• Simple, bold, stylish and elegant.

```html
<!DOCTYPE html>
<html lang="en">
<head>
<meta charset="utf-8">
<title>Colette Marvaux – Business Card</title>
<link rel="stylesheet" href="https://fonts.googleapis.com/css2?family=Pinyon+Script&family=Parisienne&family=Questrial&display=swap">
<style>
  :root {
    --olive-deep: #2c2c1c;
    --olive-mid: #4a4a2c;
    --olive-light: #6a6838;
    --ink: #000000;
    --silver: #c9c8bb;
    --silver-dark: #6e6d62;
    --paper: #ffffff;
    --text: #ffffff;
  }
  * { box-sizing: border-box; margin: 0; padding: 0; }
  html, body { width: 965px; height: 1200px; overflow: hidden; background: var(--paper); }
  .sheet { position: relative; width: 965px; height: 1200px; }
  .card { position: absolute; left: 0; width: 965px; overflow: hidden; }
  .card--front { top: 0; height: 587px; }
  .card--back { top: 607px; height: 593px; }
  .card svg { position: absolute; inset: 0; display: block; }
  .sans { font-family: "Questrial", sans-serif; fill: var(--text); }
  .script-city { font-family: "Pinyon Script", cursive; fill: var(--text); font-size: 44px; letter-spacing: 4px; }
  .tagline { font-family: "Parisienne", cursive; fill: var(--text); font-size: 44px; }
  .brand-first { font-size: 84px; letter-spacing: 3px; }
  .brand-last { font-size: 30px; letter-spacing: 9px; }
  .brand-first--small { font-size: 40px; letter-spacing: 1px; }
  .brand-last--small { font-size: 13px; letter-spacing: 4px; }
  .contact { font-size: 28px; letter-spacing: 3.2px; }
  .contact--wide { letter-spacing: 5px; }
</style>
</head>
<body>
<main class="sheet">
  <section class="card card--front" aria-label="Card front">
    <svg width="965" height="587" viewBox="0 0 965 587">
      <defs>
        <linearGradient id="oliveFront" x1="0" y1="0" x2="0" y2="1">
          <stop offset="0" stop-color="var(--olive-deep)"/>
          <stop offset="0.5" stop-color="var(--olive-mid)"/>
          <stop offset="1" stop-color="var(--olive-light)"/>
        </linearGradient>
        <linearGradient id="silverFront" x1="1" y1="0" x2="0" y2="1">
          <stop offset="0" stop-color="var(--silver-dark)"/>
          <stop offset="0.35" stop-color="var(--silver)"/>
          <stop offset="1" stop-color="var(--silver-dark)"/>
        </linearGradient>
      </defs>
      <rect class="background" width="965" height="587" fill="url(#oliveFront)"/>
      <path class="sheen" d="M0,490 C40,330 210,228 460,226 C660,224 800,190 890,118 C932,82 955,35 965,0 L965,587 L0,587 Z" fill="url(#silverFront)"/>
      <path class="field" d="M0,540 C40,370 210,248 460,240 C660,234 800,215 880,160 C925,125 952,80 965,40 L965,587 L0,587 Z" fill="var(--ink)"/>
      <text class="script-city" x="96" y="128">of Sydney</text>
      <text class="sans brand-first" x="890" y="445" text-anchor="end">Colette</text>
      <text class="sans brand-last" x="648" y="530" text-anchor="middle">MARVAUX</text>
    </svg>
  </section>

  <section class="card card--back" aria-label="Card back">
    <svg width="965" height="593" viewBox="0 0 965 593">
      <defs>
        <linearGradient id="oliveBack" x1="0" y1="0" x2="0" y2="1">
          <stop offset="0" stop-color="var(--olive-deep)"/>
          <stop offset="0.5" stop-color="var(--olive-mid)"/>
          <stop offset="1" stop-color="var(--olive-light)"/>
        </linearGradient>
        <linearGradient id="silverBack" x1="0" y1="0" x2="1" y2="1">
          <stop offset="0" stop-color="var(--silver-dark)"/>
          <stop offset="0.3" stop-color="var(--silver)"/>
          <stop offset="0.75" stop-color="var(--silver)"/>
          <stop offset="1" stop-color="var(--silver-dark)"/>
        </linearGradient>
        <path id="taglinePath" d="M118,82 C360,112 620,170 925,285"/>
      </defs>
      <rect class="background" width="965" height="593" fill="url(#oliveBack)"/>
      <path class="sheen" d="M0,20 C50,150 210,222 430,232 C660,242 840,286 920,405 C950,455 965,515 965,560 L965,593 L0,593 Z" fill="url(#silverBack)"/>
      <path class="field" d="M0,40 C40,175 200,245 420,252 C650,260 815,300 895,420 C935,480 952,540 958,593 L0,593 Z" fill="var(--ink)"/>
      <text class="tagline"><textPath href="#taglinePath">Pure pleasure for the discerning gentleman</textPath></text>
      <text class="sans brand-first--small" x="938" y="62" text-anchor="end">Colette</text>
      <text class="sans brand-last--small" x="840" y="112" text-anchor="middle">MARVAUX</text>
      <text class="sans contact" x="32" y="362">colettemarvaux.com.au</text>
      <text class="sans contact" x="32" y="426">Contact by SMS or email only :</text>
      <text class="sans contact" x="32" y="491">colette@colettemarvaux.com.au</text>
      <text class="sans contact contact--wide" x="32" y="533">Mobile : 0483 615 204 or + 61 483 615 204</text>
    </svg>
  </section>
</main>
</body>
</html>
```